Christmas Candle Label

We require a Christmas candle label that fits with our current brand (see larkvalewickworks.example, and also example attached). On the attached we would like the word 'Tovane - Mirreld' replaced with 'Merry Christmas' (or something creative that you can come up with) and the writing on the left hand side 'lose yourself in the subtle.........' replaced with 'its beginning to smell a lot like Christmas' (or something creative that you can come up with). We would like the flora image in the background replaced with a line drawing of a Christmas tree or holy or anything else that is appropriate. Finally we are not sure if a different colour label i.e. red, maroon or green (with lots of black, silver or gold writing) instead of black would be best for this label. It may be best to see a comparison of our original black label with black, silver or gold writing, and the other colours.

```html
<!DOCTYPE html>
<html lang="en">
<head>
<meta charset="utf-8">
<title>Christmas Candle Label</title>
<link rel="stylesheet" href="https://fonts.googleapis.com/css2?family=Caladea&family=Montserrat:wght@400;500&display=swap">
<style>
  :root {
    --page-bg: #f1f1f1;
    --label-black: #060606;
    --frame-line: #d9d9d9;
    --gold-text: #ece0a6;
    --white-text: #f4f4f4;
    --gold-deep: #b99a4a;
    --gold-light: #e9d891;
  }
  * { margin: 0; padding: 0; box-sizing: border-box; }
  html, body { width: 1200px; height: 849px; overflow: hidden; }
  body { background: var(--page-bg); position: relative; }

  .candle-label {
    position: absolute;
    left: 133px; top: 177px;
    width: 960px; height: 430px;
    background: var(--label-black);
  }
  .label-frame {
    position: absolute;
    inset: 9px;
    border: 1.5px solid var(--frame-line);
  }

  .seasonal-quote {
    position: absolute;
    left: 50px; top: 66px;
    font-family: "Caladea", Cambria, Georgia, serif;
    font-weight: 400;
    font-size: 28px;
    line-height: 35px;
    color: var(--gold-text);
    white-space: nowrap;
  }

  .product-title {
    position: absolute;
    left: 318px; top: 44px;
    font-family: "Montserrat", Arial, sans-serif;
    font-weight: 400;
    font-size: 25px;
    line-height: 32px;
    color: var(--white-text);
    white-space: nowrap;
  }

  .headline {
    position: absolute;
    left: 318px; top: 188px;
    font-family: "Caladea", Cambria, Georgia, serif;
    font-weight: 400;
    font-size: 42px;
    line-height: 52px;
    color: var(--gold-text);
    white-space: nowrap;
  }

  .origin-note {
    position: absolute;
    left: 318px; top: 373px;
    font-family: "Montserrat", Arial, sans-serif;
    font-size: 12px;
    color: var(--white-text);
    white-space: nowrap;
  }

  .tree-artwork {
    position: absolute;
    left: 545px; top: 52px;
    width: 230px; height: 356px;
  }

  .product-details {
    position: absolute;
    left: 813px; top: 0;
    width: 114px;
    font-family: "Montserrat", Arial, sans-serif;
    font-size: 13px;
    line-height: 16px;
    color: var(--white-text);
  }
  .batch-number { position: absolute; top: 60px; left: 0; white-space: nowrap; word-spacing: 4px; }
  .burn-info { position: absolute; top: 156px; left: 0; width: 130px; white-space: nowrap; }
  .ingredients { position: absolute; top: 273px; left: 0; width: 130px; white-space: nowrap; }
  .detail-rule { position: absolute; left: 0; width: 114px; height: 1px; background: var(--white-text); }
  .detail-rule.first { top: 250px; }
  .detail-rule.second { top: 347px; }
  .net-weight { position: absolute; top: 362px; left: 0; font-size: 17px; }
</style>
</head>
<body>
  <div class="candle-label">
    <div class="label-frame"></div>

    <p class="seasonal-quote">"Breathe in<br>the essence of<br>Christmas as<br>the scent of<br>the season<br>fills the air,<br>bringing its<br>magic to life."</p>

    <h1 class="product-title">Untamed Kestorran<br>Wilderness</h1>

    <p class="headline">The fragrance<br>of Christmas<br>is here.</p>

    <p class="origin-note">Handcrafted In Southern Kestorra</p>

    <svg class="tree-artwork" viewBox="0 0 230 356" role="img" aria-label="Gold line-drawn Christmas tree with a shining star at the top">
      <defs>
        <radialGradient id="treeGlow" cx="50%" cy="60%" r="60%">
          <stop offset="0%" stop-color="#e9d891" stop-opacity="0.5"/>
          <stop offset="100%" stop-color="#b99a4a" stop-opacity="0.1"/>
        </radialGradient>
      </defs>
      <polygon points="115,0 230,356 0,356" fill="url(#treeGlow)"/>
    </svg>

    <div class="product-details">
      <p class="batch-number">Batch No. &nbsp;/ &nbsp;/</p>
      <p class="burn-info">90+ hours<br>Hand poured<br>&nbsp;scented<br>soy and<br>coconut candle</p>
      <div class="detail-rule first"></div>
      <p class="ingredients">Made with all<br>natural<br>ingredients</p>
      <div class="detail-rule second"></div>
      <p class="net-weight">500g</p>
    </div>
  </div>
</body>
</html>
```